An expert for Professional and Technical Evaluation of Painting Work Needs a New Letterhead Design

I own a mid-sized painting company and also work as an expert for professional and technical evaluation of painting work in the area of Zurich.

Please read the project description and the must-have-requirements carefully!

I attached 1 PDF which will help you create a new letterhead design:

THE NEW DESIGN DOESN'T NEED A LOGO! (Because it won't represent a company, it represents only a service)
Updates

Dear designers We had a discussion about the location/placement of the design and came to the conclusion that we only want the design to be in the header area of the A4-paper. We would be glad to receive some revised version of your designs. Thank you and kind regards!

Project Deadline Extended
Reason: Due to the fact that only 20% of the designer have understood the brief and submitted designs that have met the requirements we decided to extend the contest deadline.

Project Deadline Extended
Reason: A great deal of good designs were submitted in the last few days. A big thank you to all the participating designers for your good work. We need a few more days to discuss some changes with certain designers and to decide which design will win.

Target Market(s)

(Insurance) Companies, partly also private clients.

Industry/Entity Type

Painting

Colors

Designer to choose colors to be used in the design.

Requirements
Must have
• All information (text, phone numbers, ...) of the old design ("old_letterhead_design.pdf") has also to be in the new one. Additional to that there are a few changes:
The phone numbers "01 583 61 47" and "01 583 61 37" change to "044 583 61 47" and "044 583 61 37". And please mention also this email address: gutachten@valmorkeller.example .

- The design should only be in the header-area of the A4-paper. An the background color of the A4-paper will be white.

- The design should consist of two designs. One for the first page and a smaller version of the design for the following pages.

- THE NEW DESIGN DOESN'T NEED A LOGO! You can make a design with geometric forms, ...

- The new design should have a juridical look. It should only contain colors like brown, fawn, black, light green, ...... colors which look serious/reliable.
Nice to have
• Geometric Forms, Symbols or other design elements.

- It would also be nice to have some design elements which emphasize the kind of work we are offering.

```html
<!DOCTYPE html>
<html lang="de">
<head>
<meta charset="utf-8">
<title>Valmor Keller – Briefpapier</title>
<link rel="stylesheet" href="https://fonts.googleapis.com/css2?family=Noto+Sans:wght@400;500&family=Arimo:wght@400&display=swap">
<style>
  :root {
    --backdrop: #e9e6e1;
    --paper: #ffffff;
    --sage: #7fa66c;
    --sage-fade: rgba(127, 166, 108, 0);
    --oxblood: #8e1b1b;
    --band: #a3262a;
    --ink: #1c1c1c;
    --band-text: #ffffff;
  }
  * { margin: 0; padding: 0; box-sizing: border-box; }
  html, body { width: 1200px; height: 900px; overflow: hidden; }
  body { background: var(--backdrop); position: relative; font-family: "Noto Sans", sans-serif; }

  .sheet {
    position: absolute; left: 300px; top: 30px;
    width: 592px; height: 838px;
    background: var(--paper);
    box-shadow: 0 2px 10px rgba(0,0,0,0.18);
  }
  .header-texture {
    position: absolute; left: 0; top: 0;
    width: 330px; height: 138px;
    background: linear-gradient(100deg, var(--sage) 0%, rgba(127,166,108,0.55) 35%, var(--sage-fade) 85%);
    -webkit-mask-image: linear-gradient(180deg, #000 0%, #000 60%, rgba(0,0,0,0.6) 100%);
  }
  .sender {
    position: absolute; right: 22px; top: 18px;
    text-align: right; color: var(--ink);
    font-size: 12.5px; line-height: 18px;
  }
  .sender-name {
    color: var(--oxblood); font-size: 19px; font-weight: 500;
    line-height: 26px; margin-bottom: 2px;
  }
  .sender-line span + span { margin-left: 18px; }
  .sender-line .zip { margin-left: 6px; }

  .service-band {
    position: absolute; left: 0; top: 138px;
    width: 100%; height: 14px;
    background: var(--band);
    display: flex; align-items: center;
    padding-left: 47px; gap: 12px;
    list-style: none;
    font-family: "Arimo", sans-serif; font-size: 11px;
    color: var(--band-text);
  }
  .service-band li { display: flex; align-items: center; margin-right: 4px; }
  .service-band li::before {
    content: ""; width: 6px; height: 6px; background: var(--band-text);
    margin-right: 6px;
  }
</style>
</head>
<body>
  <main class="sheet">
    <div class="header-texture" role="img" aria-label="Dekoratives Punktraster in Salbeigrün, nach rechts auslaufend"></div>

    <address class="sender" style="font-style:normal">
      <div class="sender-name">Valmor Keller</div>
      <div class="sender-line"><span>Eidg.dipl.Malermeister</span><span>Birkenweg 7</span><span class="zip">8805 Seewil</span></div>
      <div>Telefon : 044 583 61 47</div>
      <div>Fax : 044 583 61 37</div>
      <div>Natel : 079 412 35 90</div>
      <div>Email : gutachten@valmorkeller.example</div>
    </address>

    <ul class="service-band">
      <li>Gutachten</li>
      <li>Expertisen</li>
      <li>Devisierungen</li>
      <li>Farbberatungen</li>
      <li>Dekorative Gestaltungen</li>
    </ul>
  </main>
</body>
</html>
```